Stylish new business card needed!

Hello everyone! I am in need of a new business card design for an alarm company here in Hurricane WV. I have all fonts, color codes and logos provided for you use! We are a young company and like the style of a clean sleek looking business card. Would like it double sided, one side holding the logo and the other with your design!
Target Market(s)
The people that are looking for the newest tech for home automation and security
Industry/Entity Type
Alarm services; Home automation
Contact Information for Business Card
Name of person; position (Sales; Installer); Phone Number (555.419.7362); Employee cell Number; Website (www.GuardedByVelm.example); Employee Email; Double sided
Look and feel
Each slider illustrates characteristics of the customer's brand and the style your logo design should communicate.

```html
<!DOCTYPE html>
<html lang="en">
<head>
<meta charset="utf-8">
<title>Guarded by Velm — Business Card</title>
<link rel="stylesheet" href="https://fonts.googleapis.com/css2?family=Archivo+Black&family=Arimo:wght@400;700&display=swap">
<style>
  :root {
    --stage: #161616;
    --orange: #f4904f;
    --grey: #9b9b9b;
    --grey-dark: #8a8a8a;
    --white: #ffffff;
  }
  * { box-sizing: border-box; margin: 0; padding: 0; }
  html, body { width: 1200px; height: 780px; overflow: hidden; }
  body {
    background: var(--stage);
    display: flex;
    align-items: center;
    justify-content: center;
    gap: 40px;
    font-family: "Arimo", Arial, sans-serif;
  }
  .card {
    position: relative;
    width: 560px;
    height: 320px;
    overflow: hidden;
  }

  /* Back side */
  .card-back { background: var(--grey); }
  .card-back .pattern-area {
    position: absolute; inset: 0;
    background: linear-gradient(135deg, #a3a3a3 0%, #929292 100%);
  }
  .card-back .back-mark {
    position: absolute;
    right: 56px;
    bottom: 70px;
    color: var(--white);
    font-family: "Archivo Black", Arial, sans-serif;
    font-size: 15px;
    letter-spacing: 1px;
    line-height: 1.1;
  }

  /* Front side */
  .card-front { background: var(--orange); }
  .card-front .curve { position: absolute; inset: 0; }
  .name-block {
    position: absolute;
    left: 22px;
    top: 34px;
    padding-left: 18px;
    color: var(--white);
  }
  .name-block::before {
    content: "";
    position: absolute;
    left: 0; top: 4px;
    width: 10px; height: 52px;
    background: var(--grey);
  }
  .person-name {
    font-family: "Archivo Black", Arial, sans-serif;
    font-size: 24px;
    line-height: 1.05;
    white-space: nowrap;
  }
  .person-role {
    font-family: "Arimo", Arial, sans-serif;
    font-weight: 700;
    font-size: 14px;
    margin-top: 4px;
  }
  .contact-list {
    position: absolute;
    left: 140px;
    bottom: 24px;
    list-style: none;
    color: var(--white);
    font-size: 13px;
    line-height: 18px;
    white-space: nowrap;
  }
  .contact-list li { display: flex; align-items: center; gap: 8px; }
  .contact-list svg { width: 11px; height: 11px; flex: none; }

  .brand-lockup {
    position: absolute;
    right: 16px;
    top: 72px;
    width: 156px;
  }
  .brand-name {
    display: flex;
    align-items: center;
    gap: 8px;
    color: var(--grey-dark);
    font-family: "Archivo Black", Arial, sans-serif;
    line-height: 1;
  }
  .brand-name .dot {
    width: 30px; height: 30px;
    border-radius: 50%;
    background: var(--orange);
    flex: none;
  }
  .brand-name .words { font-size: 32px; }
  .brand-name .words small { display: block; font-size: 13px; margin-bottom: 4px; }
  .brand-tagline {
    margin-top: 10px;
    color: var(--orange);
    font-family: "Arimo", Arial, sans-serif;
    font-weight: 700;
    font-size: 7px;
    letter-spacing: 0.3px;
    white-space: nowrap;
  }
</style>
</head>
<body>

  <section class="card card-back" aria-label="Card back">
    <div class="pattern-area" role="img" aria-label="Repeating embossed brand-name pattern"></div>
    <div class="back-mark">GUARDED BY<br>VELM</div>
  </section>

  <section class="card card-front" aria-label="Card front">
    <svg class="curve" viewBox="0 0 560 320" aria-hidden="true">
      <path d="M380,0 C340,130 320,260 392,320 L560,320 L560,0 Z" fill="var(--grey)"/>
      <path d="M390,0 C352,128 334,254 404,320 L560,320 L560,0 Z" fill="var(--white)"/>
    </svg>

    <div class="name-block">
      <h1 class="person-name">Marta Kovalenko</h1>
      <p class="person-role">Sales; Installer</p>
    </div>

    <div class="brand-lockup">
      <div class="brand-name">
        <span class="dot"></span>
        <span class="words"><small>GUARDED BY</small>VELM</span>
      </div>
      <p class="brand-tagline">AUTOMATION AND SECURITY SERVICES</p>
    </div>

    <ul class="contact-list">
      <li>
        <svg viewBox="0 0 12 12"><path d="M2.5 1 L4.5 1 L5.3 3.4 L4 4.3 C4.6 5.8 6.2 7.4 7.7 8 L8.6 6.7 L11 7.5 L11 9.5 C11 10.3 10.3 11 9.5 11 C5 10.7 1.3 7 1 2.5 C1 1.7 1.7 1 2.5 1 Z" fill="var(--white)"/></svg>
        555.419.7362
      </li>
      <li>
        <svg viewBox="0 0 12 12"><rect x="3" y="0.8" width="6" height="10.4" rx="1" fill="none" stroke="var(--white)" stroke-width="1.2"/></svg>
        555.208.6614
      </li>
      <li>
        <svg viewBox="0 0 12 12"><circle cx="6" cy="6" r="5" fill="none" stroke="var(--white)" stroke-width="1.2"/><ellipse cx="6" cy="6" rx="2.2" ry="5" fill="none" stroke="var(--white)" stroke-width="1"/><line x1="1" y1="6" x2="11" y2="6" stroke="var(--white)" stroke-width="1"/></svg>
        www.GuardedByVelm.example
      </li>
      <li>
        <svg viewBox="0 0 12 12"><rect x="0.8" y="2.5" width="10.4" height="7" fill="none" stroke="var(--white)" stroke-width="1.2"/><path d="M0.8 2.5 L6 6.5 L11.2 2.5" fill="none" stroke="var(--white)" stroke-width="1.2"/></svg>
        info@GuardedByVelm.example
      </li>
    </ul>
  </section>

</body>
</html>
```